Pedicure Menu with 8 Scent Options

This design will be for a single page menu (front/back) that will display multiple different scent variations of a product. The purpose of this menu is to display to clients and show them the available options and benefits of each option.
The menu will be double sided.
The front page will include a header including brand logo and product name, and a total of 8 different scents including imagery and descriptive text.
The design should include the text provided for each scent. The design should have a layout that is structured/organized, easy to read, and has bright imagery that represents each scent.
An example is a modular layout using boxes that highlight a different scent within each box. Lavender scent should include aesthetic images of lavender flower and/or the color purple.
The back page will include brand logo, overall product description, and additional brief text that explains each step of the product.
The final size of the design should be 8.5"x11", produced in InDesign format, with all layers editable for future changes.
NOTE: Please carefully review the attached design brief that includes additional information, and all necessary text to include in the design.
Target Market(s)
Beauty/Spa Clients
Industry/Entity Type
Beauty
Requirements
Must have
- Bright and Vivid Imagery/Illustrations
Nice to have
- Background design that utilizes, lines, shapes, or other elements.

```html
<!DOCTYPE html>
<html lang="en">
<head>
<meta charset="utf-8">
<title>Lumera Deluxe Pedicure Menu</title>
<link rel="stylesheet" href="https://fonts.googleapis.com/css2?family=Allura&family=DM+Serif+Display&family=Oswald:wght@500&family=Poppins:wght@400;600&family=Montserrat:wght@500&family=Roboto+Condensed:ital@1&display=swap">
<style>
:root{
  --gold:#c6a862;--gold-light:#e7d08f;--ink:#1c1c1c;--paper:#ffffff;--stage:#ffffff;
  --lavender:#8c4fc2;--mandarin:#f7860e;--jasmine:#c8c9b0;--greentea:#8cc43f;
  --cucumber:#a3bb5a;--rose:#e6001f;--honey:#f7ce45;--mint:#65a038;
}
*{box-sizing:border-box;margin:0;padding:0}
html,body{width:1200px;height:808px;overflow:hidden;background:var(--stage)}
.page{position:absolute;top:78px;width:501px;height:648px;background:var(--paper);overflow:hidden;border:1px solid #e6e6e6}
.front{left:72px}.back{left:622px}
.header-curve{position:absolute;left:0;top:0}
.title{position:absolute;top:6px;width:100%;text-align:center;font-family:"Allura",cursive;font-size:58px;color:#fff;line-height:1}
.steps{position:absolute;top:60px;left:0;width:100%;display:flex;align-items:center;justify-content:center;gap:8px;color:#fff;font-family:"Oswald",sans-serif;font-size:23px;letter-spacing:3px}
.steps .rule{width:95px;height:2px;background:#fff;position:relative}
.steps .rule::before{content:"";position:absolute;top:-3px;width:8px;height:8px;border-radius:50%;background:#fff}
.steps .rule.l::before{left:0}.steps .rule.r::before{right:0}
.pick{position:absolute;left:161px;top:91px;width:180px;height:27px;border:3px solid var(--gold);border-radius:8px;background:#fff;font-family:"DM Serif Display",serif;font-size:16px;text-align:center;line-height:21px;color:var(--ink)}
.scent{position:absolute;width:210px;height:91px;border:2px solid var(--c);border-top:none;border-radius:0 0 6px 6px;background:#fff}
.scent-band{height:41px;background:var(--c);border-radius:6px 0 0 0;margin:0 -2px;padding:0 0 0 16px;display:flex;align-items:center;font-family:"DM Serif Display",serif;color:#fff;font-size:20px;line-height:.9}
.scent p{padding:6px 6px 0 6px;font-family:"Montserrat",sans-serif;font-size:6.6px;line-height:1.22;text-align:justify;color:var(--ink)}
.scent-photo{position:absolute;right:-14px;top:-24px;width:64px;height:64px;border-radius:50%;border:3px solid var(--c);background:#fff;padding:6px}
.scent-photo span{display:block;width:100%;height:100%;border-radius:50%;background:var(--img)}
.col-a{left:30px}.col-b{left:254px}
.r1{top:163px}.r2{top:284px}.r3{top:405px}.r4{top:526px}
.back-header{position:absolute;left:0;top:0;width:100%;height:76px;background:linear-gradient(180deg,var(--gold),var(--gold-light));border-bottom:2px solid var(--gold)}
.brand{position:absolute;top:14px;width:100%;text-align:center;font-family:"Poppins",sans-serif;font-weight:400;font-size:36px;color:#fff;letter-spacing:2px;line-height:1}
.brand small{display:block;font-size:6px;letter-spacing:3px;margin-top:2px}
.intro{position:absolute;top:86px;left:20px;right:20px;text-align:center;font-family:"Poppins",sans-serif;font-size:12.6px;line-height:15px;color:var(--ink)}
.step{position:absolute;width:179px;text-align:center}
.step-photo{position:relative;height:145px;border:3px solid var(--gold);border-radius:8px;background:var(--img)}
.step-num{position:absolute;right:-3px;top:-3px;width:30px;height:30px;background:var(--gold);border-radius:0 8px 0 8px;color:#fff;font-family:"Poppins",sans-serif;font-weight:600;font-size:22px;line-height:32px}
.step h3{margin-top:6px;font-family:"Poppins",sans-serif;font-weight:600;font-size:12px;color:var(--gold);letter-spacing:.3px}
.step p{font-family:"Poppins",sans-serif;font-size:12px;line-height:14px;color:var(--ink);padding:0 14px}
.s1{left:57px;top:148px}.s2{left:264px;top:148px}.s3{left:57px;top:356px}.s4{left:264px;top:356px}
.contact{position:absolute;left:33px;top:576px}
.icon{position:absolute;left:0;width:18px;height:18px;background:var(--gold-light);border-radius:3px}
.phone{position:absolute;left:27px;top:2px;font-family:"Oswald",sans-serif;font-size:22px;line-height:22px;color:#111;white-space:nowrap}
.address{position:absolute;left:27px;top:28px;font-family:"Roboto Condensed",sans-serif;font-style:italic;font-size:9.5px;line-height:11px;color:#111;white-space:nowrap}
.web{position:absolute;left:180px;top:575px;width:288px;text-align:center}
.web-label{font-family:"Poppins",sans-serif;font-weight:600;font-size:15px;line-height:16px;color:#111}
.web-url{margin-top:2px;height:25px;border-radius:7px;background:linear-gradient(180deg,var(--gold),var(--gold-light));border:2px solid var(--gold);font-family:"Poppins",sans-serif;font-size:15px;line-height:21px;color:#fff}
</style>
</head>
<body>
<section class="page front">
  <svg class="header-curve" width="501" height="120" viewBox="0 0 501 120">
    <defs><linearGradient id="goldfade" x1="0" y1="0" x2="0" y2="1"><stop offset="0" stop-color="#c6a862"/><stop offset="1" stop-color="#e7d08f"/></linearGradient></defs>
    <path d="M0 0H501V75Q250 140 0 75Z" fill="url(#goldfade)"/>
  </svg>
  <h1 class="title">Deluxe Pedicure</h1>
  <div class="steps"><span class="rule l"></span>4-STEP<span class="rule r"></span></div>
  <div class="pick">PICK YOUR PEDICURE</div>

  <article class="scent col-a r1" style="--c:var(--lavender)">
    <h2 class="scent-band">LAVENDER</h2>
    <p>Melt away the stresses of the day with a delicate, sweet smell that is floral and woodsy at the same time. Lavender is a calming scent for relaxation that puts us in a better mood and helps create a sense of tranquility and peacefulness.</p>
    <div class="scent-photo" style="--img:radial-gradient(#a98ad8,#5b3a9a)"><span role="img" aria-label="Bunch of lavender flowers"></span></div>
  </article>
  <article class="scent col-b r1" style="--c:var(--mandarin)">
    <h2 class="scent-band">MANDARIN</h2>
    <p>Uplift your senses with a fruity and sweet aroma that promotes clarity, radiance and a smooth, even skin tone. A citrus blend of essential oils works great to polish dull skin, reduce wrinkles, and correct spots.</p>
    <div class="scent-photo" style="--img:radial-gradient(#ffb347,#f07a0a)"><span role="img" aria-label="Three mandarin oranges"></span></div>
  </article>
  <article class="scent col-a r2" style="--c:var(--jasmine)">
    <h2 class="scent-band">JASMINE</h2>
    <p>Embrace the warmth of a rich and sensual floral scent that boosts your energy levels and helps make your day better and brighter. A symbol of purity, love, and beauty – Jasmine helps to reduce exhaustion, nervousness, and stress.</p>
    <div class="scent-photo" style="--img:radial-gradient(#ffffff,#9fbf7a)"><span role="img" aria-label="White jasmine blossoms with leaves"></span></div>
  </article>
  <article class="scent col-b r2" style="--c:var(--greentea)">
    <h2 class="scent-band">GREEN TEA</h2>
    <p>Restore a sense of serenity with fragrant green tea extract that helps to relax the mind, reduces redness and swelling, and leaves the skin feeling hydrated, silky, and smooth. A natural detoxification that will supplies abundant moisture</p>
    <div class="scent-photo" style="--img:radial-gradient(#8fd14f,#2f7d1e)"><span role="img" aria-label="Fresh green tea leaves"></span></div>
  </article>
  <article class="scent col-a r3" style="--c:var(--cucumber)">
    <h2 class="scent-band">CUCUMBER<br>MELON</h2>
    <p>Jump into a refreshing blend of crisp cucumber, watery honeydew, and summer cantaloupe. Perfect for capturing the essence of a summer day. Bamboo and aloe extract help cool your skin after a day in the sun.</p>
    <div class="scent-photo" style="--img:radial-gradient(#d9c9a0,#3f8a2a)"><span role="img" aria-label="Cantaloupe melon and cucumbers"></span></div>
  </article>
  <article class="scent col-b r3" style="--c:var(--rose)">
    <h2 class="scent-band">ROSE</h2>
    <p>Fall in love with a delicate floral twist of spicy and sweet that nourishes your skin and calms the mind. Essential oils help to reduce fine lines and protect the skin from UV damage.</p>
    <div class="scent-photo" style="--img:radial-gradient(#e0142a,#8a0010)"><span role="img" aria-label="Red rose"></span></div>
  </article>
  <article class="scent col-a r4" style="--c:var(--honey)">
    <h2 class="scent-band">MILK &amp;<br>HONEY</h2>
    <p>Discover one of nature's most luxurious skin cleansers and softeners. Creamy milk is full of rich essential vitamins that supply abundant moisture and improves skin elasticity. Sweet honey contains antioxidants and other nutrients that slow down skin aging.</p>
    <div class="scent-photo" style="--img:linear-gradient(180deg,#e9a23b 0%,#ffffff 40%,#eeeeee 100%)"><span role="img" aria-label="Glass of milk with honey dipper"></span></div>
  </article>
  <article class="scent col-b r4" style="--c:var(--mint)">
    <h2 class="scent-band">MINT</h2>
    <p>Rejuvenate your body with a cool mix of peppermint and spearmint that prevents skin damage, alleviates inflamed skin, and acts as a splash of tonic for the senses. Infused with eucalyptus to leave you clean, cool, and crisp.</p>
    <div class="scent-photo" style="--img:radial-gradient(#7ccf5a,#2e7a28)"><span role="img" aria-label="Sprig of mint leaves"></span></div>
  </article>
</section>

<section class="page back">
  <header class="back-header">
    <div class="brand">Lumera<small>BEAUTY &amp; SPA</small></div>
  </header>
  <p class="intro">Lumera Deluxe Pedicure 4-Step will transform your pedicure experience and immerse your senses into a floral paradise designed to rejuvenate your body. Sit back, relax, and enjoy.</p>

  <div class="step s1">
    <div class="step-photo" role="img" aria-label="Feet soaking in a copper bowl" style="--img:linear-gradient(160deg,#7a4a34,#c98f5c 55%,#8a5a36)"><span class="step-num">1</span></div>
    <h3>SALT SOAK</h3><p>Detoxifies and deodorizes your feet.</p>
  </div>
  <div class="step s2">
    <div class="step-photo" role="img" aria-label="Hands applying sugar scrub to a foot" style="--img:linear-gradient(160deg,#f3f3f3,#e6c6ad 60%,#f5f5f5)"><span class="step-num">2</span></div>
    <h3>SUGAR SCRUB</h3><p>Gently exfoliates dead skin.</p>
  </div>
  <div class="step s3">
    <div class="step-photo" role="img" aria-label="Leg covered in foot masque" style="--img:linear-gradient(150deg,#9a6a4e,#c79b7e 55%,#8a8a8a)"><span class="step-num">3</span></div>
    <h3>FOOT MASQUE</h3><p>Cleanses pores for smoother skin.</p>
  </div>
  <div class="step s4">
    <div class="step-photo" role="img" aria-label="Hands massaging lotion into a leg" style="--img:linear-gradient(150deg,#8a6f80,#d2a88a 55%,#9a8a80)"><span class="step-num">4</span></div>
    <h3>MASSAGE LOTION</h3><p>Hydrates and soothes skin.</p>
  </div>

  <div class="contact">
    <svg class="icon" style="top:4px" viewBox="0 0 18 18"><rect width="18" height="18" rx="3" fill="#e7d08f"/><path d="M5 4l2.5 0 1 3-1.5 1a7 7 0 0 0 3 3l1-1.5 3 1V13a1 1 0 0 1-1 1A9 9 0 0 1 4 5a1 1 0 0 1 1-1z" fill="#fff"/></svg>
    <span class="phone">XXX-XXX-XXX</span>
    <svg class="icon" style="top:28px" viewBox="0 0 18 18"><rect width="18" height="18" rx="3" fill="#e7d08f"/><path d="M9 3a4 4 0 0 1 4 4c0 3-4 8-4 8S5 10 5 7a4 4 0 0 1 4-4z" fill="#fff"/><circle cx="9" cy="7" r="1.6" fill="#e7d08f"/></svg>
    <span class="address">Lorem ipsum dolor sit amet,<br>consectetuer adipiscing elit.</span>
  </div>
  <div class="web">
    <div class="web-label">visit our website</div>
    <div class="web-url">www.lumeraspa-demo.com</div>
  </div>
</section>
</body>
</html>
```